A4 Single Page Brochure for Private Cloud Offerings

Theme: Futuristic Tech Company

Brightmoor Systems is looking to offer private cloud services for our enterprise customers in Perth-based data-centres that provides our clients with a lower-cost alternative to Nimbra or KLT yielding better performance.

We are looking for a single A4 brochure with a great graphics design theme to promote these services.

We will be providing five tiers:
- Starter
- Growth
- Professional
- Premier
- Elite

Each plan must list on the brochure the Max VMs, CPU cores, Memory and SSD storage allocated. Refer to the uploaded PNG file.

The brochure must list the following selling points:

- Hosted in a local Perth-based TIER3 and TIER4 datacentres
- WA owned hosting - support local
- Low latency - ultra fast local hosting
- Includes Quorra Host Datacentre licensing
- Includes WallHaven Managed Firewalls for Enterprise level threat detection
- Includes all infrastructure maintenance services
- Full self management of VMs through customer portal
- Includes a 1gbps Internet link
- Predictable fixed monthly fee with no dynamic billing
- No additional charges for Storage Transactions, Internet Usage, VM Snapshots, Datacentre Bandwidth Usage and Firewall Traffic Usage.
- Highly available cluster, no single point of failure.
- Pricing is based on 36 months commit
- Yearly rate increases capped to a maximum of Australian CPI
- All plans have 24/7/365 support with dedicated after hours number.
- Managed backup and managed disaster recovery services can be added to plans

Service provided in accordance with our terms and conditions.

We need the ability to EDIT the brochure to adjust pricing after we receive the final project.

Please do not utilise "Pushing the Boundaries of Technology" - our brand is being replaced with "Specialised Consulting". New website is under development but not launched yet.

Target Market(s)

Information Technology Sector

Colors
0054AA
0677BA
7BADD7
CADEEF
E8F1F8

Requirements
Must have
• Theme of Brightmoor is Blue
Should not have
• Extremely stock imagary that just looks "cheap and stock"

```html
<!DOCTYPE html>
<html lang="en">
<head>
<meta charset="utf-8">
<title>Brightmoor Systems – Private Cloud Brochure</title>
<link href="https://fonts.googleapis.com/css2?family=Bebas+Neue&family=Montserrat:wght@400;500;600;700;800&display=swap" rel="stylesheet">
<style>
:root{
  --stage:#3b3a3e;
  --paper:#ffffff;
  --navy:#1b2a80;
  --royal:#1f4bb5;
  --sky:#5b8fd0;
  --pale:#7badd7;
  --row-light:#6f9fd9;
  --row-dark:#2058c0;
  --grey:#b9bbbf;
  --ink:#1c1c1c;
}
*{margin:0;padding:0;box-sizing:border-box}
html,body{width:880px;height:1200px;overflow:hidden;background:var(--stage)}
body{position:relative;font-family:"Montserrat",Arial,sans-serif}
.sheet{position:absolute;top:308px;width:415px;height:583px;overflow:hidden;box-shadow:0 6px 16px rgba(0,0,0,.45)}
.sheet--front{left:17px}
.sheet--back{left:448px}
.page{position:absolute;left:0;top:0;width:607px;height:852px;background:var(--paper);transform:scale(.6837);transform-origin:0 0}
.layer{position:absolute;left:0;top:0;width:607px;height:852px}

/* brand */
.brand{position:absolute;left:120px;top:58px;display:flex;align-items:center;gap:14px}
.brand__mark{width:34px;height:34px;background:var(--navy)}
.brand__name{font-weight:700;font-size:34px;color:var(--navy);letter-spacing:1px}

/* headline */
.headline{position:absolute;left:44px;top:386px;font-family:"Bebas Neue",Impact,sans-serif;line-height:.9}
.headline__lead{display:block;font-size:31px;color:var(--royal)}
.headline__mid{display:block;font-size:38px;color:var(--royal)}
.headline__main{display:block;font-size:86px;color:var(--navy);letter-spacing:-1px;margin-top:2px}
.tiers-intro{position:absolute;left:42px;top:524px;font-family:"Bebas Neue",Impact,sans-serif;font-size:27px;color:var(--sky)}

/* tiers */
.tier{position:absolute;width:150px;margin-left:-75px;text-align:center}
.tier__badge{width:80px;height:80px;margin:0 auto;border-radius:50%;background:radial-gradient(circle at 50% 40%,#3a6fd6,#1d3aa0);border:5px solid #8fb6e6;display:flex;align-items:center;justify-content:center}
.tier__name{margin-top:8px;font-weight:600;font-size:15px;color:var(--ink);letter-spacing:.3px}

/* footer */
.footer{position:absolute;left:0;bottom:0;width:607px;height:50px;background:var(--navy);border-top:6px solid var(--pale);color:#fff}
.footer__info{position:absolute;left:44px;top:7px;font-size:8.5px;font-weight:700;line-height:16px}
.footer__info span{display:flex;align-items:center;gap:6px}
.footer__phone{position:absolute;right:36px;top:8px;font-size:22px;font-weight:800;display:flex;align-items:center;gap:6px}

/* pricing */
.pricing{position:absolute;left:42px;top:376px;width:522px;table-layout:fixed;border-collapse:collapse;font-size:10.5px}
.pricing th{font-weight:700;color:var(--ink);font-size:11px;text-align:center;padding:0 0 5px;height:22px;vertical-align:bottom}
.pricing td{color:#fff;height:22px;padding:0 6px;border:2px solid #fff}
.pricing td.label{text-align:left;font-weight:500}
.pricing td.num{text-align:right}
.pricing tr.light td{background:var(--row-light)}
.pricing tr.dark td{background:var(--row-dark)}
.cost{position:absolute;top:500px;font-size:11px;font-weight:600;color:var(--ink)}
.note{position:absolute;left:42px;top:528px;font-size:10.5px;color:var(--ink)}

/* features */
.features{position:absolute;top:576px;list-style:none}
.features--left{left:47px;width:245px}
.features--right{left:316px;width:250px}
.features li{position:relative;padding:0 0 2px 18px;margin-bottom:5px;font-size:10.5px;line-height:1.12;color:var(--royal);border-bottom:1px dotted #555}
.features li svg{position:absolute;left:0;top:2px}
</style>
</head>
<body>

<!-- FRONT -->
<section class="sheet sheet--front">
  <div class="page">
    <svg class="layer" viewBox="0 0 607 852" aria-hidden="true">
      <polygon points="0,345 607,45 607,115 225,374 0,400" fill="var(--grey)"/>
    </svg>
    <svg class="layer" viewBox="0 0 607 852" role="img" aria-label="Glowing digital network held in an open hand">
      <defs><linearGradient id="netGlow" x1="0" y1="0" x2="1" y2="1"><stop offset="0" stop-color="#1a1f7a"/><stop offset=".6" stop-color="#2f5fd0"/><stop offset="1" stop-color="#152a8a"/></linearGradient></defs>
      <polygon points="0,95 190,252 0,345" fill="url(#netGlow)"/>
    </svg>
    <svg class="layer" viewBox="0 0 607 852" role="img" aria-label="Hand touching a tablet screen with a glowing interface">
      <defs><linearGradient id="tabletShot" x1="0" y1="0" x2="1" y2="1"><stop offset="0" stop-color="#d9dadc"/><stop offset=".55" stop-color="#8d98a8"/><stop offset="1" stop-color="#3d4a5e"/></linearGradient></defs>
      <polygon points="225,374 607,115 607,585" fill="url(#tabletShot)"/>
    </svg>

    <div class="brand"><span class="brand__mark"></span><span class="brand__name">BRIGHTMOOR</span></div>

    <h1 class="headline">
      <span class="headline__lead">PERTH PRIVATE CLOUD</span>
      <span class="headline__mid">SPECIALISED</span>
      <span class="headline__main">CONSULTING</span>
    </h1>
    <p class="tiers-intro">WE WILL BE PROVIDING FVE TIERS :</p>

    <div class="tier" style="left:135px;top:578px"><div class="tier__badge" role="img" aria-label="Starter tier icon"></div><p class="tier__name">STARTER</p></div>
    <div class="tier" style="left:305px;top:578px"><div class="tier__badge"><svg width="40" height="36" viewBox="0 0 40 36" fill="none" stroke="#fff" stroke-width="2"><path d="M2 34h36"/><rect x="6" y="22" width="6" height="12"/><rect x="16" y="16" width="6" height="18"/><rect x="26" y="10" width="6" height="24"/><path d="M4 18 L30 4 M24 3h7v6"/></svg></div><p class="tier__name">GROWTH</p></div>
    <div class="tier" style="left:468px;top:578px"><div class="tier__badge" role="img" aria-label="Professional tier icon"></div><p class="tier__name">PROFESSIONAL</p></div>
    <div class="tier" style="left:215px;top:683px"><div class="tier__badge" role="img" aria-label="Premier tier icon"></div><p class="tier__name">PREMIER</p></div>
    <div class="tier" style="left:386px;top:683px"><div class="tier__badge" role="img" aria-label="Elite tier icon"></div><p class="tier__name">ELITE</p></div>

    <footer class="footer">
      <div class="footer__info">
        <span><svg width="10" height="10" viewBox="0 0 10 10" fill="none" stroke="#fff"><circle cx="5" cy="5" r="4.3"/><path d="M.7 5h8.6M5 .7c-2.4 2.4-2.4 6.2 0 8.6M5 .7c2.4 2.4 2.4 6.2 0 8.6"/></svg>www.brightmoorsystems.com.au</span>
        <span><svg width="10" height="11" viewBox="0 0 10 11" fill="none" stroke="#fff"><path d="M5 10S1.3 6.2 1.3 4A3.7 3.7 0 0 1 8.7 4C8.7 6.2 5 10 5 10z"/><circle cx="5" cy="4" r="1.3"/></svg>12/4 Harbour Crescent,Coogee Bay6166Australia</span>
      </div>
      <div class="footer__phone"><svg width="16" height="16" viewBox="0 0 16 16"><circle cx="8" cy="8" r="8" fill="#fff"/><path d="M5.3 4.2l1.4 1.9-.8 1c.6 1.2 1.5 2.1 2.7 2.7l1-.8 1.9 1.4-.9 1.5C8.2 11.7 4.4 7.9 4 5.1z" fill="var(--navy)"/></svg>08 9000 4182</div>
    </footer>
  </div>
</section>

<!-- BACK -->
<section class="sheet sheet--back">
  <div class="page">
    <svg class="layer" viewBox="0 0 607 852" role="img" aria-label="Futuristic grid of glowing data blocks under an orange light">
      <defs>
        <radialGradient id="dataGlow" cx=".5" cy=".33" r=".7"><stop offset="0" stop-color="#f0b35a"/><stop offset=".25" stop-color="#d3772a"/><stop offset=".5" stop-color="#2a8fc8"/><stop offset=".8" stop-color="#0d4a7a"/><stop offset="1" stop-color="#062033"/></radialGradient>
      </defs>
      <rect x="0" y="0" width="607" height="355" fill="url(#dataGlow)"/>
    </svg>

    <table class="pricing">
      <colgroup><col style="width:115px"><col style="width:70px"><col style="width:77px"><col style="width:108px"><col style="width:82px"><col style="width:70px"></colgroup>
      <thead><tr><th></th><th>Starter</th><th>Growth</th><th>Professional</th><th>Premier</th><th>Elite</th></tr></thead>
      <tbody>
        <tr class="light"><td class="label">Max VMs</td><td class="num">5</td><td class="num">10</td><td class="num">15</td><td class="num">20</td><td class="num">25</td></tr>
        <tr class="dark"><td class="label">CPU cores</td><td class="num">8</td><td class="num">16</td><td class="num">32</td><td class="num">48</td><td class="num">64</td></tr>
        <tr class="light"><td class="label">Memory (GB)</td><td class="num">64</td><td class="num">128</td><td class="num">192</td><td class="num">256</td><td class="num">320</td></tr>
        <tr class="dark"><td class="label">Storage SSD (TB)</td><td class="num">3</td><td class="num">6</td><td class="num">15</td><td class="num">20</td><td class="num">30</td></tr>
      </tbody>
    </table>

    <span class="cost" style="left:42px">Monthly Cost</span>
    <span class="cost" style="left:167px">$&nbsp;&nbsp;1,028.01</span>
    <span class="cost" style="left:262px">$&nbsp;&nbsp;3, 426.64</span>
    <span class="cost" style="left:365px">$&nbsp;&nbsp;&nbsp;5,482.72</span>
    <span class="cost" style="left:475px">$&nbsp;&nbsp;&nbsp;&nbsp;7,196.07</span>
    <p class="note">For larger plans, ask us.</p>

    <ul class="features features--left">
      <li><svg width="9" height="9" viewBox="0 0 9 9"><circle cx="4.5" cy="4.5" r="4.5" fill="#222"/><path d="M2.4 4.6l1.4 1.4 2.8-2.8" stroke="#fff" stroke-width="1.2" fill="none"/></svg>Hosted in a local Perth-based TIER3 and TIER4 datacentres</li>
      <li><svg width="9" height="9" viewBox="0 0 9 9"><circle cx="4.5" cy="4.5" r="4.5" fill="#222"/><path d="M2.4 4.6l1.4 1.4 2.8-2.8" stroke="#fff" stroke-width="1.2" fill="none"/></svg>WA owned hosting - support local</li>
      <li><svg width="9" height="9" viewBox="0 0 9 9"><circle cx="4.5" cy="4.5" r="4.5" fill="#222"/><path d="M2.4 4.6l1.4 1.4 2.8-2.8" stroke="#fff" stroke-width="1.2" fill="none"/></svg>Low latency - ultra fast local hosting</li>
      <li><svg width="9" height="9" viewBox="0 0 9 9"><circle cx="4.5" cy="4.5" r="4.5" fill="#222"/><path d="M2.4 4.6l1.4 1.4 2.8-2.8" stroke="#fff" stroke-width="1.2" fill="none"/></svg>Includes Quorra Host Datacentre licensing</li>
      <li><svg width="9" height="9" viewBox="0 0 9 9"><circle cx="4.5" cy="4.5" r="4.5" fill="#222"/><path d="M2.4 4.6l1.4 1.4 2.8-2.8" stroke="#fff" stroke-width="1.2" fill="none"/></svg>Includes WallHaven Managed Firewalls for Enterprise level threat detection</li>
      <li><svg width="9" height="9" viewBox="0 0 9 9"><circle cx="4.5" cy="4.5" r="4.5" fill="#222"/><path d="M2.4 4.6l1.4 1.4 2.8-2.8" stroke="#fff" stroke-width="1.2" fill="none"/></svg>Includes all infrastructure maintenance services</li>
      <li><svg width="9" height="9" viewBox="0 0 9 9"><circle cx="4.5" cy="4.5" r="4.5" fill="#222"/><path d="M2.4 4.6l1.4 1.4 2.8-2.8" stroke="#fff" stroke-width="1.2" fill="none"/></svg>Full self management of VMs through customer portal</li>
    </ul>
    <ul class="features features--right">
      <li><svg width="9" height="9" viewBox="0 0 9 9"><circle cx="4.5" cy="4.5" r="4.5" fill="#222"/><path d="M2.4 4.6l1.4 1.4 2.8-2.8" stroke="#fff" stroke-width="1.2" fill="none"/></svg>Includes a 1gbps Internet link</li>
      <li><svg width="9" height="9" viewBox="0 0 9 9"><circle cx="4.5" cy="4.5" r="4.5" fill="#222"/><path d="M2.4 4.6l1.4 1.4 2.8-2.8" stroke="#fff" stroke-width="1.2" fill="none"/></svg>Predictable fixed monthly fee with no dynamic billing</li>
      <li><svg width="9" height="9" viewBox="0 0 9 9"><circle cx="4.5" cy="4.5" r="4.5" fill="#222"/><path d="M2.4 4.6l1.4 1.4 2.8-2.8" stroke="#fff" stroke-width="1.2" fill="none"/></svg>No additional charges for Storage</li>
      <li><svg width="9" height="9" viewBox="0 0 9 9"><circle cx="4.5" cy="4.5" r="4.5" fill="#222"/><path d="M2.4 4.6l1.4 1.4 2.8-2.8" stroke="#fff" stroke-width="1.2" fill="none"/></svg>Transactions, Internet Usage, VM</li>
      <li><svg width="9" height="9" viewBox="0 0 9 9"><circle cx="4.5" cy="4.5" r="4.5" fill="#222"/><path d="M2.4 4.6l1.4 1.4 2.8-2.8" stroke="#fff" stroke-width="1.2" fill="none"/></svg>Snapshots, Datacentre Bandwidth Usage and Firewall Traffic Usage.</li>
      <li><svg width="9" height="9" viewBox="0 0 9 9"><circle cx="4.5" cy="4.5" r="4.5" fill="#222"/><path d="M2.4 4.6l1.4 1.4 2.8-2.8" stroke="#fff" stroke-width="1.2" fill="none"/></svg>Pricing is based on 36 months commit</li>
      <li><svg width="9" height="9" viewBox="0 0 9 9"><circle cx="4.5" cy="4.5" r="4.5" fill="#222"/><path d="M2.4 4.6l1.4 1.4 2.8-2.8" stroke="#fff" stroke-width="1.2" fill="none"/></svg>All plans have 24/7/365 support with dedicated after hours number.</li>
      <li><svg width="9" height="9" viewBox="0 0 9 9"><circle cx="4.5" cy="4.5" r="4.5" fill="#222"/><path d="M2.4 4.6l1.4 1.4 2.8-2.8" stroke="#fff" stroke-width="1.2" fill="none"/></svg>Managed backup and managed disaster recovery services can be added to plans</li>
    </ul>

    <footer class="footer">
      <div class="footer__info">
        <span><svg width="10" height="10" viewBox="0 0 10 10" fill="none" stroke="#fff"><circle cx="5" cy="5" r="4.3"/><path d="M.7 5h8.6M5 .7c-2.4 2.4-2.4 6.2 0 8.6M5 .7c2.4 2.4 2.4 6.2 0 8.6"/></svg>www.brightmoorsystems.com.au</span>
        <span><svg width="10" height="11" viewBox="0 0 10 11" fill="none" stroke="#fff"><path d="M5 10S1.3 6.2 1.3 4A3.7 3.7 0 0 1 8.7 4C8.7 6.2 5 10 5 10z"/><circle cx="5" cy="4" r="1.3"/></svg>12/4 Harbour Crescent,Coogee Bay6166Australia</span>
      </div>
      <div class="footer__phone"><svg width="16" height="16" viewBox="0 0 16 16"><circle cx="8" cy="8" r="8" fill="#fff"/><path d="M5.3 4.2l1.4 1.9-.8 1c.6 1.2 1.5 2.1 2.7 2.7l1-.8 1.9 1.4-.9 1.5C8.2 11.7 4.4 7.9 4 5.1z" fill="var(--navy)"/></svg>08 9000 4182</div>
    </footer>
  </div>
</section>

</body>
</html>
```